Business card for builder specialising in renovations.

Need a card for our building business. Business name is under Marcus Pellow.
Have licence number on card ( 527196K)
Contact number (0400 583 214)
Want to work on logo for some business cards and shirts - something with MP or MPB or open to ideas??
No animations, No hammers. Something sharp and eye catching.
Highlight that we are a renovation specialist. Simple on front with extra details on back with some lines to jot down things.

Target Market(s)

Renovators

Industry/Entity Type

Building

Contact Information for Business Card

2 sided with room on back to jot things down.
Extra details on back so front can be simple ..like, renovations, bathrooms, decks, extensions, new builds,

Logo Text

MP

Font styles to use
Serif

Requirements
Must have
• Eye catching design .
• Name : Marcus pellow
• Licence number
• Contact number - 0400583214
Nice to have
• Some logo design that we can carry through to other forms of advertising
• Local builder
• Quality work
Should not have
• No animations

```html
<!DOCTYPE html>
<html lang="en">
<head>
<meta charset="utf-8">
<title>Marcus Pellow – Business Card</title>
<link rel="stylesheet" href="https://fonts.googleapis.com/css2?family=Arimo:wght@400;500&display=swap">
<style>
  :root {
    --backdrop: #d6dedd;
    --ink: #1b1b1c;
    --paper: #ffffff;
    --rule: #2a2a2a;
    --muted: #3a3a3a;
  }
  * { box-sizing: border-box; margin: 0; padding: 0; }
  html, body { width: 1200px; height: 1200px; overflow: hidden; }
  body {
    background: var(--backdrop);
    font-family: "Arimo", Arial, sans-serif;
    position: relative;
  }
  .card {
    position: absolute;
    left: 250px;
    width: 700px;
    height: 400px;
    overflow: hidden;
    box-shadow: 0 10px 30px rgba(0,0,0,0.18);
  }

  /* Front */
  .card--front { top: 120px; background: var(--ink); color: var(--paper); }
  .front__rule-top {
    position: absolute; left: 70px; top: 128px; width: 300px; height: 3px; background: var(--paper);
  }
  .front__name {
    position: absolute; left: 70px; top: 138px; width: 560px;
    font-size: 66px; font-weight: 500; letter-spacing: 1px; line-height: 1; white-space: nowrap;
  }
  .front__rule-bottom {
    position: absolute; left: 330px; top: 212px; width: 300px; height: 3px; background: var(--paper);
  }
  .front__tagline {
    position: absolute; left: 180px; top: 236px;
    font-size: 20px; letter-spacing: 0.5px;
  }
  .dot { display: inline-block; width: 7px; height: 7px; border-radius: 50%; background: currentColor; margin: 0 14px; vertical-align: middle; }

  /* Back */
  .card--back { top: 650px; background: var(--paper); color: var(--ink); }
  .back__name {
    position: absolute; left: 30px; top: 18px;
    font-size: 38px; font-weight: 500; letter-spacing: 0.5px; line-height: 1;
  }
  .back__name-rule { position: absolute; left: 30px; top: 62px; width: 300px; height: 3px; background: var(--ink); }
  .back__tagline { position: absolute; left: 60px; top: 70px; font-size: 11px; }
  .back__tagline .dot { width: 4px; height: 4px; margin: 0 8px; }
  .back__specialist {
    position: absolute; right: 28px; top: 22px; text-align: right;
  }
  .back__specialist-title { font-size: 20px; letter-spacing: 1px; }
  .back__licence { font-size: 11px; margin-top: 4px; }

  .back__band {
    position: absolute; left: 0; top: 96px; width: 100%; height: 96px; background: var(--ink);
  }
  .back__phone {
    position: absolute; left: 0; right: 0; top: 132px;
    display: flex; align-items: center; gap: 10px; padding: 0 30px;
    color: var(--paper); font-size: 15px; letter-spacing: 0.5px;
  }
  .back__phone .line { flex: 1; height: 1px; background: var(--paper); }
  .back__phone svg { width: 24px; height: 20px; }

  .back__connector { position: absolute; left: 60px; top: 268px; width: 580px; height: 3px; background: var(--ink); }
  .photo {
    position: absolute; width: 190px; height: 110px;
    border: 3px solid var(--ink); outline: 2px solid var(--paper);
  }
  .photo--kitchen { left: 25px; top: 160px; background: linear-gradient(135deg, #5a3a22, #b37a45 55%, #3b2a1e); }
  .photo--bathroom { left: 255px; top: 200px; background: linear-gradient(135deg, #8a6a35, #d9b46a 50%, #a5a08c); }
  .photo--living { left: 485px; top: 240px; background: linear-gradient(135deg, #4b5a52, #c9ccc8 55%, #6d6a62); }

  .back__foot-thick { position: absolute; left: 0; top: 364px; width: 100%; height: 8px; background: var(--ink); }
  .back__foot-thin { position: absolute; left: 0; top: 380px; width: 100%; height: 2px; background: var(--ink); }
</style>
</head>
<body>

  <section class="card card--front" aria-label="Business card front">
    <div class="front__rule-top"></div>
    <div class="front__name">MARCUS PELLOW</div>
    <div class="front__rule-bottom"></div>
    <div class="front__tagline">Local builder<span class="dot"></span>Quality work</div>
  </section>

  <section class="card card--back" aria-label="Business card back">
    <div class="back__name">MARCUS PELLOW</div>
    <div class="back__name-rule"></div>
    <div class="back__tagline">Local builder<span class="dot"></span>Quality work</div>

    <div class="back__specialist">
      <div class="back__specialist-title">RENOVATION SPECIALIST</div>
      <div class="back__licence">Licence number: 527196K</div>
    </div>

    <div class="back__band"></div>
    <div class="back__phone">
      <span class="line"></span>
      <svg viewBox="0 0 24 20" aria-hidden="true">
        <path d="M2 7c0-3 5-5 10-5s10 2 10 5l-4 1-1-3H7L6 8z" fill="#fff"/>
        <path d="M6 9h12l3 9H3z" fill="#fff"/>
        <g fill="#1b1b1c">
          <rect x="9" y="11" width="2" height="2"/><rect x="13" y="11" width="2" height="2"/>
          <rect x="9" y="14" width="2" height="2"/><rect x="13" y="14" width="2" height="2"/>
        </g>
      </svg>
      <span>0400 583 214</span>
      <span class="line"></span>
    </div>

    <div class="back__connector"></div>
    <div class="photo photo--kitchen" role="img" aria-label="Photo of a renovated timber kitchen"></div>
    <div class="photo photo--bathroom" role="img" aria-label="Photo of a renovated bathroom with glass shower"></div>
    <div class="photo photo--living" role="img" aria-label="Photo of a renovated modern living room"></div>

    <div class="back__foot-thick"></div>
    <div class="back__foot-thin"></div>
  </section>

</body>
</html>
```